Premium Lawn fertiliser packaging - Looking for long term designer

*Update at bottom
I need a carefully considered, bold and professional packaging design for my new premium lawn fertiliser product. This contest is for a detailed front of the stand-up pouch packaging and once I’ve chosen a winner, they’ll be asked to create the layout for the back that links to the front as well. I have a full range of additional products that will also need designs and so I'm looking for someone who can do a great job here and who we can work with long term.

The front should include our logo for Brindley Turf Supply Direct and be titled “Meadow Rise Max” "Professional Lawn Fertiliser". The spring fertiliser tag line is "Awaken your lawn: Lush Greening, Lasting Health".
Beneath it, it then needs to include some important usage information and the key benefits along with some suitable graphic.

Key information to include:

Apply March - June
Treats 35-50 m2
16-3-8
+2%MgO + 1% Fe + 2.9% CaO (this is the chemical makeup of the fertiliser and needs to be fairly prominent. If you look at other professional fertiliser packaging, you'll see how it needs to compare).

Key features:
Premium fertiliser, used by professionals
Advanced greening with micro-nutrient complex
Dual action Nitrogen: Instant green boost & continuous feed for 3 months
Child & pet safe

Our brand colours are purple and green. Purple = #592999, Green = 3cb64a / 81d742 / 4d9d44

I think these colours look great against a white background.

Please make sure you look at our website as well to get an idea of our brand: www.brindleyturfsupply.co.uk

To help, I've attached images of competitors fertiliser packaging that I like the look of. I'm not looking for you to copy but just see what type of thing appeals to me, the standard I'm expecting and what I need to compete against....

In addition, I have also attached some potential images you may wish to try using in your design, although please feel free to use your own if you have something better. For the moment, the images are 'preview' images, but once I decide on a design and we agree on the correct image, I will download and send over a fully licensed version.

*** Update*** When submitting your design, can you submit it in 2 formats: The first as a fully printed custom stand-up pouch and the second as a full-size label stuck onto a standup pouch (whatever colour you think is right for your design - choose white if you are not sure). To explain, I've just discovered we won't be able to get full custom bags printed in time for the first run and so we will have to opt for the design to be printed on labels and fixed onto bags. I therefore need to choose a design that works in both formats as both a label on a standup pouch as well as a fully printed pouch. Many thanks.

Target Market(s)

Domestic home-owners

Industry/Entity Type

Lawn care. NOT AGRICULTURE OR FARMING

Font styles to use
Sans Serif

Requirements
Must have
• Presented in 2 formats - see update at bottom of description
Nice to have
• I quite like designs against a white background, although I’m open to other ideas as well.
Should not have
• Please do not include any people or faces in the design. The text should be solid in colour, so no graduated colour fill in the text or outline text. Please avoid over-busy or cluttered designs.

```html
<!DOCTYPE html>
<html lang="en">
<head>
<meta charset="utf-8">
<title>Meadow Rise Max – Professional Lawn Fertiliser Label</title>
<link href="https://fonts.googleapis.com/css2?family=Rubik:ital,wght@0,300;0,500;0,700;0,900;1,600&display=swap" rel="stylesheet">
<style>
  :root {
    --purple: #592999;
    --purple-deep: #4a2185;
    --green: #3cb64a;
    --green-light: #81d742;
    --green-dark: #4d9d44;
    --white: #ffffff;
    --stage: #f4f4f2;
    --ink: #2b2b2b;
  }
  * { box-sizing: border-box; margin: 0; padding: 0; }
  html, body {
    width: 1200px; height: 777px; overflow: hidden;
    background: var(--stage);
    font-family: "Rubik", sans-serif;
  }
  .label {
    position: absolute;
    left: 345px; top: 18px;
    width: 510px; height: 740px;
    background: var(--white);
    box-shadow: 0 4px 18px rgba(0,0,0,.12);
    overflow: hidden;
  }
  .brand {
    position: absolute; top: 26px; left: 0; width: 100%;
    display: flex; align-items: center; justify-content: center; gap: 10px;
  }
  .brand-dot { width: 22px; height: 22px; border-radius: 50%; background: var(--green); }
  .brand-name {
    font-family: "Rubik", sans-serif; font-weight: 500;
    font-size: 19px; color: var(--purple); letter-spacing: .5px;
  }
  .product-title {
    position: absolute; top: 86px; left: 40px;
    color: var(--purple); font-weight: 900;
    font-size: 70px; line-height: .88; letter-spacing: -1px;
  }
  .product-title .accent { color: var(--green); font-weight: 300; }
  .lawn-photo {
    position: absolute; left: 200px; top: 215px; width: 310px; height: 400px;
    background: linear-gradient(180deg, #dfe7ee 0%, #9aa6b3 30%, #8a7f6d 48%, #4d8a3b 65%, #3f8a32 100%);
    border-radius: 60% 0 0 40% / 20% 0 0 30%;
  }
  .swoosh {
    position: absolute; left: 0; top: 560px; width: 510px; height: 100px;
  }
  .type-banner {
    position: absolute; left: 40px; top: 250px; width: 340px; height: 120px;
  }
  .type-banner svg { position: absolute; inset: 0; }
  .type-banner .text {
    position: absolute; left: 16px; top: 10px; color: var(--white);
    font-weight: 700; line-height: 1;
  }
  .type-banner .small { font-size: 22px; display: block; }
  .type-banner .big { font-size: 54px; font-weight: 900; display: block; margin: 2px 0; }
  .tagline {
    position: absolute; left: 52px; top: 395px;
    font-style: italic; font-weight: 600; font-size: 19px; line-height: 1.2;
  }
  .tagline .mark { color: var(--green); font-size: 30px; position: absolute; left: -10px; top: -18px; font-style: normal; }
  .tagline .l1 { color: var(--purple); }
  .tagline .l2 { color: var(--green); }
  .tagline .l3 { color: var(--purple); }
  .usage-box {
    position: absolute; left: 42px; top: 478px; width: 118px; height: 160px;
  }
  .usage-box svg { position: absolute; inset: 0; }
  .usage-box .content { position: absolute; left: 10px; top: 8px; width: 98px; color: var(--purple); }
  .usage-box .season { font-size: 10px; font-weight: 700; border-bottom: 1px solid var(--purple); padding-bottom: 4px; }
  .usage-box .treats { font-size: 8px; font-weight: 500; margin-top: 5px; }
  .usage-box .area { font-size: 24px; font-weight: 900; line-height: 1; }
  .usage-box .area sup { font-size: 12px; }
  .usage-box .npk { font-size: 17px; font-weight: 500; border-top: 1px solid var(--purple); border-bottom: 1px solid var(--purple); margin-top: 4px; padding: 2px 0; text-align: center; }
  .usage-box .extras { font-size: 7px; font-weight: 700; margin-top: 4px; text-align: center; }
  .safe-badge {
    position: absolute; right: 20px; top: 545px; width: 62px; text-align: center;
    color: var(--white);
  }
  .safe-badge .disc { width: 50px; height: 50px; margin: 0 auto 4px; border-radius: 50%; background: var(--white); border: 3px solid var(--purple); }
  .safe-badge .word { font-size: 19px; font-weight: 900; line-height: 1; color: var(--white); }
  .safe-badge .sub { font-size: 7px; font-weight: 700; background: var(--white); color: var(--purple); padding: 1px 2px; margin-top: 2px; }
  .benefits {
    position: absolute; left: 20px; top: 640px; width: 470px; height: 72px;
    background: var(--purple);
    display: flex; align-items: center; padding: 0 10px; gap: 8px;
  }
  .benefit { flex: 1; display: flex; gap: 5px; color: var(--white); font-size: 10px; line-height: 1.15; padding-right: 6px; }
  .benefit + .benefit { border-left: 1.5px solid var(--white); padding-left: 8px; }
  .benefit svg { flex: none; margin-top: 1px; }
  .benefit b { display: block; font-weight: 900; text-transform: uppercase; }
  .benefit .hl { color: var(--green-light); font-weight: 900; text-transform: uppercase; }
</style>
</head>
<body>
<main class="label">
  <header class="brand">
    <span class="brand-dot"></span>
    <span class="brand-name">Brindley Turf Supply Direct</span>
  </header>

  <h1 class="product-title">MEADOW<br>RISE <span class="accent">MAX</span></h1>

  <div class="lawn-photo" role="img" aria-label="Photo of a stone manor house with slate roof behind a round, striped green lawn and colourful flower beds"></div>

  <svg class="swoosh" viewBox="0 0 510 100" preserveAspectRatio="none" aria-hidden="true">
    <path d="M0 40 Q200 -10 510 30 L510 100 L0 100 Z" fill="var(--green)"/>
  </svg>

  <div class="type-banner">
    <svg viewBox="0 0 340 120" preserveAspectRatio="none" aria-hidden="true">
      <path d="M0 0 H290 L340 30 L260 120 H0 Z" fill="var(--green-light)"/>
      <path d="M0 0 H250 V120 H0 Z" fill="var(--green)"/>
    </svg>
    <div class="text">
      <span class="small">PROFESSIONAL</span>
      <span class="big">LAWN</span>
      <span class="small">FERTILISER</span>
    </div>
  </div>

  <p class="tagline">
    <span class="mark">“</span>
    <span class="l1">Awaken Your Lawn</span><br>
    <span class="l2">Lush Greening,</span><br>
    <span class="l3">Lasting Health</span>
  </p>

  <div class="usage-box">
    <svg viewBox="0 0 118 160" preserveAspectRatio="none" aria-hidden="true">
      <path d="M2 2 H116 V140 L59 158 L2 140 Z" fill="var(--white)" stroke="var(--purple)" stroke-width="3"/>
    </svg>
    <div class="content">
      <p class="season">Apply March - June</p>
      <p class="treats">Treats</p>
      <p class="area">35-50m<sup>2</sup></p>
      <p class="npk">16 - 03 - 08</p>
      <p class="extras">2% MgO + 1% Fe + 2.9% CaO</p>
    </div>
  </div>

  <div class="safe-badge">
    <div class="disc"></div>
    <p class="word">SAFE</p>
    <p class="sub">PETS &amp; KIDS</p>
  </div>

  <section class="benefits">
    <div class="benefit">
      <svg width="12" height="10" viewBox="0 0 12 10"><path d="M1 5 L4.5 8.5 L11 1" fill="none" stroke="var(--green-light)" stroke-width="2"/></svg>
      <p><b>Premium Fertiliser</b>used by professionals</p>
    </div>
    <div class="benefit">
      <svg width="12" height="10" viewBox="0 0 12 10"><path d="M1 5 L4.5 8.5 L11 1" fill="none" stroke="var(--green-light)" stroke-width="2"/></svg>
      <p><b>Advanced</b><span class="hl">Greening</span><br>with micro-nutrient complex</p>
    </div>
    <div class="benefit">
      <svg width="12" height="10" viewBox="0 0 12 10"><path d="M1 5 L4.5 8.5 L11 1" fill="none" stroke="var(--green-light)" stroke-width="2"/></svg>
      <p><b>Dual Action Nitrogen</b>Instant green boost &amp; continuous feed for 3 months</p>
    </div>
  </section>
</main>
</body>
</html>
```